Harwell Lawyers Banner

I would like to have a graphic design created for a company banner. The company is Harwell Lawyers and the website is https://harwelllawyers-example.com.au/ We would like a professional banner we are able to put up at events to advertise the company.
The banner size is 800mm wide by 2000mm high so please keep the design inside these constraints.

```html
<!DOCTYPE html>
<html lang="en">
<head>
<meta charset="utf-8">
<title>Harwell Lawyers – Event Banner</title>
<link href="https://fonts.googleapis.com/css2?family=Montserrat:wght@300;400;500;700&display=swap" rel="stylesheet">
<style>
  :root {
    --page: #e4e4e4;
    --banner-top: #141414;
    --banner-mid: #2a2a2a;
    --white: #ffffff;
    --muted: #cfcfcf;
    --gold: #f2b705;
    --photo-dark: #0c0c0c;
    --photo-light: #5a5a5a;
  }
  * { margin: 0; padding: 0; box-sizing: border-box; }
  html, body {
    width: 1200px; height: 900px; overflow: hidden;
    background: var(--page);
    font-family: "Montserrat", Arial, sans-serif;
  }
  .banner {
    position: absolute; left: 428px; top: 20px;
    width: 344px; height: 860px; overflow: hidden;
    background: linear-gradient(180deg, var(--banner-top) 0%, #1f1f1f 35%, var(--banner-mid) 62%, #1a1a1a 100%);
    color: var(--white);
  }
  .brand {
    position: absolute; right: 34px; top: 52px;
    text-align: right; color: var(--white); font-weight: 300;
  }
  .brand-name { display: block; font-size: 44px; letter-spacing: 2px; line-height: 1; }
  .brand-sub { display: block; font-size: 17px; letter-spacing: 5px; margin-top: 8px; }
  .intro {
    position: absolute; left: 30px; top: 176px; width: 300px;
    font-size: 20.5px; font-weight: 400; line-height: 29px;
  }
  .intro strong { font-weight: 700; }
  .feature { position: absolute; top: 336px; width: 135px; }
  .feature.help { left: 30px; }
  .feature.services { left: 192px; }
  .feature-icon { width: 30px; height: 30px; display: block; }
  .feature-title { margin-top: 14px; font-size: 12.5px; font-weight: 700; line-height: 17px; min-height: 34px; }
  .feature-label { margin-top: 6px; font-size: 7.5px; font-weight: 400; text-transform: uppercase; color: var(--muted); }
  .feature-text { margin-top: 12px; font-size: 7.8px; line-height: 11.6px; color: var(--muted); }
  .photo {
    position: absolute; left: 0; right: 0; top: 610px; bottom: 0;
    background:
      radial-gradient(ellipse 60% 55% at 60% 35%, var(--photo-light) 0%, #2e2e2e 45%, transparent 75%),
      linear-gradient(180deg, transparent 0%, var(--photo-dark) 100%);
  }
  .contact { position: absolute; left: 178px; top: 552px; list-style: none; }
  .contact li {
    display: flex; align-items: flex-start; gap: 7px;
    font-size: 7.8px; font-weight: 700; line-height: 11px; margin-bottom: 6px;
  }
  .contact svg { width: 9px; height: 9px; flex: none; margin-top: 1px; }
</style>
</head>
<body>
  <main class="banner">
    <div class="brand">
      <span class="brand-name">HARWELL</span>
      <span class="brand-sub">LAWYERS</span>
    </div>

    <p class="intro">Harwell Lawyers is a leading commercial law firm located in Logan City, <strong>Queensland</strong>.</p>

    <section class="feature help">
      <svg class="feature-icon" viewBox="0 0 30 30" fill="none" stroke="var(--gold)" stroke-width="1.6">
        <path d="M3 10 L15 3 L27 10 Z"/>
        <path d="M4 12 H26 M6 13 V23 M11 13 V23 M19 13 V23 M24 13 V23 M3 25 H27 M2 28 H28"/>
      </svg>
      <h2 class="feature-title">How Can We Help You?</h2>
      <p class="feature-label">What best describes you</p>
      <p class="feature-text">Need advice? We take the time to understand your situation to ensure you get the best outcomes.</p>
    </section>

    <section class="feature services">
      <svg class="feature-icon" viewBox="0 0 30 30" fill="none" stroke="var(--gold)" stroke-width="1.6">
        <path d="M15 2 L26 6 V14 C26 21 21 26 15 28 C9 26 4 21 4 14 V6 Z"/>
        <path d="M10 15 L14 19 L21 11"/>
      </svg>
      <h2 class="feature-title">What We Do</h2>
      <p class="feature-label">Services</p>
      <p class="feature-text">From tax structures to estate planning, startups to established enterprises, you get access to our experienced team of law professionals to guide you through the maze of law.</p>
    </section>

    <div class="photo" role="img" aria-label="Black and white photo of hands reviewing documents on a desk"></div>

    <ul class="contact">
      <li>
        <svg viewBox="0 0 10 10"><path fill="var(--gold)" d="M2 0.5 L3.6 2.6 L2.8 3.8 C3.4 5.2 4.8 6.6 6.2 7.2 L7.4 6.4 L9.5 8 L8.4 9.6 C4.5 9.4 0.6 5.5 0.4 1.6 Z"/></svg>
        <span>07 3000 4182</span>
      </li>
      <li>
        <svg viewBox="0 0 10 10"><rect x="0.5" y="2" width="9" height="6.5" fill="var(--gold)"/><path d="M0.5 2 L5 5.6 L9.5 2" fill="none" stroke="#222" stroke-width="0.9"/></svg>
        <span>info@harwelllawyers-example.com.au</span>
      </li>
      <li>
        <svg viewBox="0 0 10 10"><path fill="var(--gold)" d="M5 0.3 C2.9 0.3 1.4 1.9 1.4 3.8 C1.4 6.4 5 9.8 5 9.8 C5 9.8 8.6 6.4 8.6 3.8 C8.6 1.9 7.1 0.3 5 0.3 Z"/><circle cx="5" cy="3.8" r="1.3" fill="#222"/></svg>
        <span>Harbour Court, Unit 8<br>1450 Marlow Road<br>Kingsford, QLD 4000</span>
      </li>
    </ul>
  </main>
</body>
</html>
```